Redesign Website for Tandara Flame

I have an existing website on https://www.tandaraflame-example.com.au/ and would like to have this redesigned professionally with new content (please refer to word document). We are fire protection engineers providing fire services design expertise and engineering design to a range of different clients.

We also provide drafting services to clients in the form of completing final commissioning documentation such as 'as-installed' drawings and fire services block plans to ensure compliance with the building code and relevant Australian Standards.

Target Market(s)

Builders, Architects, Consultants, Project Managers

Industry/Entity Type

Engineering Consultant

Coding

Coded - Design and coding required

Number of Pages Required

4 page

Font styles to use
Sans Serif

Requirements
Must have
• Home and about Page, fire services design page, fire block plans page, contact us page (4 Pages).

The website colour choice must match or compliment the new company logo.
Nice to have
• Quality photos of fire services installations in buildings to Australian Standards.

A website similar to this would be ideal http://corbellpyro-example.com.au
Should not have
• Stolen licensed photos

```html
<!DOCTYPE html>
<html lang="en">
<head>
<meta charset="utf-8">
<title>Tandara Flame — Fire Services Drawings &amp; Block Plans</title>
<link href="https://fonts.googleapis.com/css2?family=Jost:wght@400;500;600;700&display=swap" rel="stylesheet">
<style>
:root{
  --orange:#f7941d;
  --orange-soft:#fde6c8;
  --ink:#1f2128;
  --text:#555a63;
  --muted:#8a8f98;
  --bg-soft:#eef1f7;
  --white:#ffffff;
  --hero-dark:#2e5a86;
  --hero-light:#b9cbe0;
  --btn-grey:#a3a6ab;
}
*{box-sizing:border-box;margin:0;padding:0}
html,body{width:1200px;height:4640px;overflow:hidden}
body{font-family:"Jost",sans-serif;color:var(--ink);background:var(--white)}
.page{position:relative;width:1200px;height:4640px;overflow:hidden}
.abs{position:absolute}

/* header */
.brand{position:absolute;display:flex;align-items:center;gap:10px;font-family:"Jost",sans-serif;font-weight:600;color:var(--orange);letter-spacing:1px}
.brand-dot{width:18px;height:18px;border-radius:50%;background:var(--orange)}
.nav{position:absolute;top:54px;left:505px;display:flex;align-items:center;gap:42px;font-size:20px;color:var(--white)}
.nav-cta{background:var(--orange);padding:9px 28px;border-radius:26px;margin-left:-8px}

/* hero */
.hero-photo{position:absolute;left:0;top:0;width:1200px;height:800px;background:linear-gradient(110deg,var(--hero-dark) 0%,#4d77a3 40%,var(--hero-light) 75%,#c7d3e2 100%)}
.hero-title{position:absolute;left:117px;top:240px;color:var(--white);font-weight:700;font-size:64px;letter-spacing:1px;line-height:1}
.hero-sub{position:absolute;left:117px;top:318px;color:var(--white);font-weight:600;font-size:48px;line-height:1}
.hero-text{position:absolute;left:117px;top:396px;color:var(--white);font-size:25px;line-height:37px;width:480px}
.hero-btn{position:absolute;left:117px;top:516px;width:184px;height:50px;border-radius:25px;background:var(--white);color:var(--ink);font-weight:700;font-size:16px;display:flex;align-items:center;justify-content:center}
.dots{position:absolute;left:566px;top:657px;display:flex;gap:8px}
.dots span{width:15px;height:15px;border-radius:50%;background:var(--white)}
.dots .on{background:var(--orange);border:2px solid var(--white)}

/* stats + about */
.stat{position:absolute;width:216px;height:200px;text-align:center}
.stat svg{position:absolute;left:0;top:0;filter:drop-shadow(0 4px 10px rgba(0,0,0,.08))}
.stat-body{position:relative;padding-top:30px}
.stat-num{font-size:28px;font-weight:500;margin-top:6px}
.stat-label{font-size:14px;color:var(--muted)}
.about-title{position:absolute;left:654px;top:918px;font-size:46px;font-weight:600}
.about-text{position:absolute;left:654px;top:985px;width:370px;font-size:14.5px;line-height:24px;color:var(--text)}

/* section headings */
.eyebrow{position:absolute;width:1200px;text-align:center;color:var(--orange);font-size:22px}
.heading{position:absolute;width:1200px;text-align:center;font-size:44px;font-weight:400}
.heading b{font-weight:700}

/* service cards */
.svc{position:absolute;width:296px;height:166px;background:var(--white);box-shadow:0 4px 12px rgba(0,0,0,.12);overflow:hidden}
.svc-name{position:absolute;left:28px;top:54px;width:230px;font-size:17px;font-weight:500;line-height:26px;color:#333}
.svc-corner{position:absolute;right:-30px;bottom:-30px;width:110px;height:110px;border-radius:50%;background:var(--orange-soft)}
.svc-icon{position:absolute;right:22px;bottom:22px;width:46px;height:46px;border:3px solid var(--orange);border-radius:50%}
.svc.active{background:var(--orange)}
.svc.active .svc-name{color:var(--white)}
.svc.active .svc-corner{background:#f9a746}
.svc.active .svc-icon{border-color:var(--white)}
.pill-grey{position:absolute;left:501px;top:2016px;width:196px;height:50px;border-radius:25px;background:var(--btn-grey);color:var(--white);font-size:16px;display:flex;align-items:center;justify-content:center}

/* drawings */
.drawings{position:absolute;left:0;top:2156px;width:1200px;height:648px;background:var(--orange)}
.dr-label{position:absolute;width:263px;text-align:center;color:var(--white);font-size:18px}
.dr-frame{position:absolute;width:263px;height:234px;background:var(--white);padding:6px;box-shadow:0 4px 12px rgba(0,0,0,.15)}
.dr-fill{width:100%;height:100%;background:linear-gradient(135deg,#d9dde6,#eef0f4 55%,#c9cfdb)}
.dr-btn{position:absolute;width:152px;height:36px;border-radius:18px;background:var(--white);color:var(--orange);font-size:15px;font-weight:500;display:flex;align-items:center;justify-content:center}

/* block plans */
.plan{position:absolute;width:297px;height:261px;text-align:center}
.plan svg.hex{position:absolute;left:0;top:0;filter:drop-shadow(0 5px 12px rgba(0,0,0,.12))}
.plan-inner{position:relative;display:flex;flex-direction:column;align-items:center;height:100%;justify-content:center}
.plan-icon{width:78px;height:62px;border-radius:8px;background:#dcdfe5;margin-bottom:16px}
.plan-name{font-size:18px;font-weight:500;line-height:24px;color:#333}
.plan.active .plan-name{color:var(--white)}

/* reviews */
.reviews{position:absolute;left:0;top:3655px;width:1200px;height:645px;background:var(--bg-soft)}
.review{position:absolute;width:292px;height:310px;background:var(--white);border-radius:16px;box-shadow:0 4px 14px rgba(0,0,0,.08);padding:42px 40px 0}
.review h3{font-size:21px;font-weight:600;line-height:27px}
.review p{font-size:14px;line-height:24px;color:var(--text);margin-top:20px}
.reviewer{position:absolute;left:40px;top:240px;display:flex;align-items:center;gap:12px}
.avatar{width:44px;height:44px;border-radius:50%;background:linear-gradient(135deg,#c9b3a3,#7b5e52)}
.stars{color:var(--orange);font-size:14px;letter-spacing:1px;line-height:14px}
.reviewer-name{font-size:13px;font-weight:600}

/* footer */
.foot-h{position:absolute;font-size:17px;color:#333;letter-spacing:.5px}
.foot-list{position:absolute;font-size:15px;line-height:24px;color:#444}
.foot-row{display:flex;gap:12px;align-items:flex-start;margin-bottom:16px}
.social{position:absolute;left:140px;top:4458px;display:flex;gap:10px}
.social span{width:32px;height:32px;border-radius:50%;background:var(--orange)}
.map{position:absolute;left:785px;top:4392px;width:281px;height:108px;background:linear-gradient(135deg,#d8e2ea,#e9eef2 60%,#d3dfd4)}
.foot-line{position:absolute;left:0;top:4548px;width:1200px;height:1px;background:#e2e4e8}
.copy{position:absolute;top:4577px;font-size:14px;color:#666}
</style>
</head>
<body>
<div class="page">

  <!-- HERO -->
  <div class="hero-photo" role="img" aria-label="Photo of a red fire alarm call point mounted on a wall"></div>
  <svg class="abs" style="left:0;top:620px" width="1200" height="200" viewBox="0 0 1200 200">
    <path d="M0 30 C220 70 420 120 600 165 C800 110 1000 40 1200 10 L1200 200 L0 200 Z" fill="#ffffff"/>
    <path d="M430 128 C500 150 560 162 600 168 C650 158 720 135 780 112" stroke="#f7941d" stroke-width="4" fill="none"/>
    <path d="M0 30 C220 70 420 120 600 165" stroke="#dfe8f2" stroke-width="8" fill="none" opacity=".6"/>
  </svg>

  <div class="brand" style="left:63px;top:93px;font-size:23px"><span class="brand-dot"></span>TANDARA FLAME</div>
  <nav class="nav">
    <span>Home</span><span>About</span><span>Fire Services</span><span>Fire Block</span><span class="nav-cta">Contact Us</span>
  </nav>

  <h1 class="hero-title">FIRE SERVICES</h1>
  <div class="hero-sub">Drawings &amp; Block Plans</div>
  <p class="hero-text">We pride ourselves on our prompt service and delivery of all of our projects.</p>
  <div class="hero-btn">LEARN MORE</div>
  <div class="dots"><span></span><span class="on"></span><span></span></div>

  <!-- STATS -->
  <div class="stat" style="left:198px;top:832px">
    <svg width="216" height="200" viewBox="0 0 216 200"><polygon points="108,4 210,52 210,148 108,196 6,148 6,52" fill="#fff"/></svg>
    <div class="stat-body">
      <svg width="40" height="44" viewBox="0 0 40 44"><circle cx="20" cy="13" r="10" fill="#f7941d"/><path d="M2 44 C2 30 10 25 20 25 C30 25 38 30 38 44 Z" fill="#f7941d"/></svg>
      <div class="stat-num">200 +</div><div class="stat-label">Total Clients</div>
    </div>
  </div>
  <div class="stat" style="left:378px;top:942px">
    <svg width="216" height="200" viewBox="0 0 216 200"><polygon points="108,4 210,52 210,148 108,196 6,148 6,52" fill="#fff"/></svg>
    <div class="stat-body">
      <svg width="40" height="44" viewBox="0 0 40 44"><circle cx="20" cy="13" r="10" fill="#f7941d"/><path d="M2 44 C2 30 10 25 20 25 C30 25 38 30 38 44 Z" fill="#f7941d"/></svg>
      <div class="stat-num">200 +</div><div class="stat-label">Total Clients</div>
    </div>
  </div>
  <div class="stat" style="left:194px;top:1042px">
    <svg width="216" height="200" viewBox="0 0 216 200"><polygon points="108,4 210,52 210,148 108,196 6,148 6,52" fill="#fff"/></svg>
    <div class="stat-body">
      <svg width="40" height="44" viewBox="0 0 40 44"><circle cx="20" cy="13" r="10" fill="#f7941d"/><path d="M2 44 C2 30 10 25 20 25 C30 25 38 30 38 44 Z" fill="#f7941d"/></svg>
      <div class="stat-num">200 +</div><div class="stat-label">Total Clients</div>
    </div>
  </div>

  <h2 class="about-title">About the Service</h2>
  <p class="about-text">Brenlow Software is a mobile-first, Field Service Management &amp; CRM Software for Contractors and Home Improvement Professionals. Our software helps commercial and residential HVAC, plumbing, electrical, and other field service businesses, to send Estimates, Invoices, collect payments, manage clients and jobs from their mobile devices.</p>

  <!-- SERVICES -->
  <div class="abs" style="left:0;top:1280px;width:1200px;height:880px;background:var(--bg-soft)"></div>
  <svg class="abs" style="left:0;top:1278px" width="1200" height="150" viewBox="0 0 1200 150">
    <path d="M0 0 L1200 0 L1200 150 C900 70 400 30 0 14 Z" fill="#ffffff"/>
  </svg>
  <div class="abs" style="left:580px;top:1343px;width:40px;height:40px;border-radius:50%;background:var(--orange);border:4px solid #fff;box-shadow:0 2px 6px rgba(0,0,0,.12)"></div>

  <div class="eyebrow" style="top:1453px">Our Services</div>
  <h2 class="heading" style="top:1484px">Fire <b>Services Drawings</b></h2>

  <div class="svc" style="left:131px;top:1602px"><div class="svc-corner"></div><div class="svc-icon"></div><div class="svc-name">Automatic Smoke Detection and Alarm System</div></div>
  <div class="svc active" style="left:451px;top:1602px"><div class="svc-corner"></div><div class="svc-icon"></div><div class="svc-name">Emergency Warning and Intercom System</div></div>
  <div class="svc" style="left:771px;top:1602px"><div class="svc-corner"></div><div class="svc-icon"></div><div class="svc-name">Occupant Warning System</div></div>
  <div class="svc" style="left:131px;top:1791px"><div class="svc-corner"></div><div class="svc-icon"></div><div class="svc-name" style="top:66px">Smoke Alarms</div></div>
  <div class="svc" style="left:451px;top:1791px"><div class="svc-corner"></div><div class="svc-icon"></div><div class="svc-name" style="top:66px">Fire Hose Reels</div></div>
  <div class="svc" style="left:771px;top:1791px"><div class="svc-corner"></div><div class="svc-icon"></div><div class="svc-name" style="top:66px">Portable Fire Extinguishers</div></div>

  <div class="pill-grey">View all Services</div>

  <!-- DRAWINGS -->
  <section class="drawings">
    <svg class="abs" style="left:566px;top:0" width="68" height="38" viewBox="0 0 68 38"><polygon points="0,0 68,0 34,38" fill="#eef1f7"/></svg>
    <div class="eyebrow" style="top:86px;color:#fff">Our Services</div>
    <h2 class="heading" style="top:116px;color:#fff">Fire <b>Services Drawings</b></h2>

    <svg class="abs" style="left:72px;top:348px" width="30" height="24" viewBox="0 0 30 24"><path d="M28 12 H3 M13 2 L3 12 L13 22" stroke="#fff" stroke-width="2.5" fill="none"/></svg>
    <svg class="abs" style="left:1096px;top:348px" width="30" height="24" viewBox="0 0 30 24"><path d="M2 12 H27 M17 2 L27 12 L17 22" stroke="#fff" stroke-width="2.5" fill="none"/></svg>

    <div class="dr-label" style="left:148px;top:206px">Marrow Lane Cinema</div>
    <div class="dr-frame" style="left:148px;top:242px"><div class="dr-fill" role="img" aria-label="Sample fire services floor plan drawing"></div></div>
    <div class="dr-btn" style="left:204px;top:508px">Learn More</div>

    <div class="dr-label" style="left:468px;top:206px">Marrow Lane Cinema</div>
    <div class="dr-frame" style="left:468px;top:242px"><div class="dr-fill" role="img" aria-label="Sample fire services floor plan drawing"></div></div>
    <div class="dr-btn" style="left:524px;top:508px">Learn More</div>

    <div class="dr-label" style="left:787px;top:206px">Marrow Lane Cinema</div>
    <div class="dr-frame" style="left:787px;top:242px"><div class="dr-fill" role="img" aria-label="Sample fire services floor plan drawing"></div></div>
    <div class="dr-btn" style="left:843px;top:508px">Learn More</div>
  </section>

  <!-- BLOCK PLANS -->
  <div class="eyebrow" style="top:2893px">Our Plans</div>
  <h2 class="heading" style="top:2922px">Fire <b>Block Plans</b></h2>

  <div class="plan" style="left:132px;top:3033px">
    <svg class="hex" width="297" height="261" viewBox="0 0 297 261"><polygon points="76,4 221,4 293,130 221,257 76,257 4,130" fill="#fff"/></svg>
    <div class="plan-inner"><div class="plan-icon" role="img" aria-label="Zone detector icon"></div><div class="plan-name">Zone Block Plans</div>
      <svg width="36" height="36" viewBox="0 0 36 36" style="margin-top:14px"><circle cx="18" cy="18" r="16" stroke="#333" stroke-width="2" fill="none"/><path d="M11 15 L18 22 L25 15" stroke="#333" stroke-width="2" fill="none"/></svg></div>
  </div>
  <div class="plan active" style="left:452px;top:3033px">
    <svg class="hex" width="297" height="261" viewBox="0 0 297 261"><polygon points="76,4 221,4 293,130 221,257 76,257 4,130" fill="#f7941d"/></svg>
    <div class="plan-inner">
      <svg width="80" height="66" viewBox="0 0 80 66" style="margin-bottom:16px"><path d="M8 22 H22 L40 6 V60 L22 44 H8 Z" stroke="#fff" stroke-width="3" fill="none" stroke-linejoin="round"/><path d="M52 20 C58 28 58 38 52 46 M62 12 C72 24 72 42 62 54" stroke="#fff" stroke-width="3" fill="none" stroke-linecap="round"/></svg>
      <div class="plan-name">EWIS/SSISEP<br>Block Plans</div>
      <svg width="36" height="36" viewBox="0 0 36 36" style="margin-top:8px"><circle cx="18" cy="18" r="16" stroke="#fff" stroke-width="2" fill="none"/><path d="M11 15 L18 22 L25 15" stroke="#fff" stroke-width="2" fill="none"/></svg></div>
  </div>
  <div class="plan" style="left:771px;top:3033px">
    <svg class="hex" width="297" height="261" viewBox="0 0 297 261"><polygon points="76,4 221,4 293,130 221,257 76,257 4,130" fill="#fff"/></svg>
    <div class="plan-inner"><div class="plan-icon" role="img" aria-label="Sprinkler head icon"></div><div class="plan-name">Sprinkler Block Plans</div>
      <svg width="36" height="36" viewBox="0 0 36 36" style="margin-top:14px"><circle cx="18" cy="18" r="16" stroke="#333" stroke-width="2" fill="none"/><path d="M11 15 L18 22 L25 15" stroke="#333" stroke-width="2" fill="none"/></svg></div>
  </div>
  <div class="plan" style="left:292px;top:3317px">
    <svg class="hex" width="297" height="261" viewBox="0 0 297 261"><polygon points="76,4 221,4 293,130 221,257 76,257 4,130" fill="#fff"/></svg>
    <div class="plan-inner"><div class="plan-icon" role="img" aria-label="Fire hydrant icon"></div><div class="plan-name">Fire Hydrant Block Plans</div>
      <svg width="36" height="36" viewBox="0 0 36 36" style="margin-top:14px"><circle cx="18" cy="18" r="16" stroke="#333" stroke-width="2" fill="none"/><path d="M11 15 L18 22 L25 15" stroke="#333" stroke-width="2" fill="none"/></svg></div>
  </div>
  <div class="plan" style="left:611px;top:3317px">
    <svg class="hex" width="297" height="261" viewBox="0 0 297 261"><polygon points="76,4 221,4 293,130 221,257 76,257 4,130" fill="#fff"/></svg>
    <div class="plan-inner"><div class="plan-icon" role="img" aria-label="Evacuation icon"></div><div class="plan-name">Evacuation Management<br>Plan /&nbsp; Diagrams</div>
      <svg width="36" height="36" viewBox="0 0 36 36" style="margin-top:8px"><circle cx="18" cy="18" r="16" stroke="#333" stroke-width="2" fill="none"/><path d="M11 15 L18 22 L25 15" stroke="#333" stroke-width="2" fill="none"/></svg></div>
  </div>

  <!-- REVIEWS -->
  <section class="reviews">
    <h2 class="heading" style="top:86px">Client <b>Reviews</b></h2>
    <svg class="abs" style="left:72px;top:308px" width="30" height="24" viewBox="0 0 30 24"><path d="M28 12 H3 M13 2 L3 12 L13 22" stroke="#555" stroke-width="2.5" fill="none"/></svg>
    <svg class="abs" style="left:1096px;top:308px" width="30" height="24" viewBox="0 0 30 24"><path d="M2 12 H27 M17 2 L27 12 L17 22" stroke="#2d6fd6" stroke-width="2.5" fill="none"/></svg>

    <div class="review" style="left:132px;top:180px">
      <h3>Lorem Ipsum is simply dummy text of the</h3>
      <p>Lorem Ipsum is simply dummy text of the printing and typesetting industry. Lorem Ipsum has been the industry's</p>
      <div class="reviewer"><div class="avatar" role="img" aria-label="Reviewer portrait"></div><div><div class="stars">★★★★★</div><div class="reviewer-name">JANE CORLISS</div></div></div>
    </div>
    <div class="review" style="left:453px;top:180px">
      <h3>Lorem Ipsum is simply dummy text of the</h3>
      <p>Lorem Ipsum is simply dummy text of the printing and typesetting industry. Lorem Ipsum has been the industry's</p>
      <div class="reviewer"><div class="avatar" role="img" aria-label="Reviewer portrait"></div><div><div class="stars">★★★★★</div><div class="reviewer-name">JANE CORLISS</div></div></div>
    </div>
    <div class="review" style="left:774px;top:180px">
      <h3>Lorem Ipsum is simply dummy text of the</h3>
      <p>Lorem Ipsum is simply dummy text of the printing and typesetting industry. Lorem Ipsum has been the industry's</p>
      <div class="reviewer"><div class="avatar" role="img" aria-label="Reviewer portrait"></div><div><div class="stars">★★★★★</div><div class="reviewer-name">JANE CORLISS</div></div></div>
    </div>
  </section>

  <!-- FOOTER -->
  <div class="brand" style="left:140px;top:4398px;font-size:20px"><span class="brand-dot" style="width:14px;height:14px"></span>TANDARA FLAME</div>
  <div class="social"><span></span><span></span><span></span><span></span></div>

  <div class="foot-h" style="left:353px;top:4355px">CONTACT US</div>
  <div class="foot-list" style="left:353px;top:4390px;width:210px;font-size:13.5px;line-height:19px">
    <div class="foot-row">
      <svg width="14" height="18" viewBox="0 0 14 18" style="flex:none;margin-top:2px"><path d="M7 17 C3 11 1 8.5 1 6.5 A6 6 0 0 1 13 6.5 C13 8.5 11 11 7 17 Z" fill="#555"/><circle cx="7" cy="6.5" r="2.2" fill="#fff"/></svg>
      <span>42 Harbour Row, Suite 3<br>Geelong VIC 3220</span></div>
    <div class="foot-row">
      <svg width="16" height="16" viewBox="0 0 16 16" style="flex:none;margin-top:2px"><path d="M3 1 L6 1 L7 5 L5 6.5 C6 9 7 10 9.5 11 L11 9 L15 10 L15 13 C15 14 14 15 13 15 C6 15 1 10 1 3 C1 2 2 1 3 1 Z" fill="#555"/></svg>
      <span>(03) 5550 1234</span></div>
    <div class="foot-row">
      <svg width="16" height="12" viewBox="0 0 16 12" style="flex:none;margin-top:4px"><rect x="0.5" y="0.5" width="15" height="11" fill="#555"/><path d="M1 1 L8 7 L15 1" stroke="#fff" stroke-width="1.3" fill="none"/></svg>
      <span>info@tandaraflame-example.com.au</span></div>
  </div>

  <div class="foot-h" style="left:598px;top:4355px">COMPANY</div>
  <div class="foot-list" style="left:598px;top:4390px">Home<br>About Us<br>Fire Services<br>Fire Block<br>Contact Us</div>

  <div class="foot-h" style="left:782px;top:4355px">LOCATION</div>
  <div class="map" role="img" aria-label="Map showing the office location"></div>
  <svg class="abs" style="left:916px;top:4426px" width="16" height="22" viewBox="0 0 16 22"><path d="M8 21 C3 14 1 11 1 7.5 A7 7 0 0 1 15 7.5 C15 11 13 14 8 21 Z" fill="#e0322b"/><circle cx="8" cy="7.5" r="2.6" fill="#fff"/></svg>

  <div class="foot-line"></div>
  <div class="copy" style="left:131px">© 2021 Tandara Flame. All Rights Reserved.</div>
  <div class="copy" style="left:894px">Privacy Policy &nbsp; | &nbsp; Terms of Use</div>
</div>
</body>
</html>
```